Application Dashboard Skin - Non coded theme only

We are looking for a website color theme/look feel for a new .net dashboard application we are building. Target audience who will be using this are E and C level professionals. We are looking for the following:

Images of optional color themes for our existing dashboard. You can access a temporary version with no styling here: http://demo.plexaroni-app.com:99/ . Application built in telerik and highcharts.

We are not looking for finished code or application skins. Our development team will take your final design (with specific colors/images/etc. provided) and apply it to the final beta version of the application.

Design considerations:
We are open to creative ideas, but please know that preference will be given to professional designs with emphasis on a consistent brand look/feel. Designs and colors should be focused on quickly identifying and processing the data.

Multiple submissions welcome.

-Quorventa team

Target Market(s)

IT / Insurance

Industry/Entity Type

Building

Number of Pages Required

3 page

Requirements
Must have
• Application Dashboard link for design: http://demo.plexaroni-app.com:99/

```html
<!DOCTYPE html>
<html lang="en">
<head>
<meta charset="utf-8">
<title>Auditwell – Dashboard</title>
<link href="https://fonts.googleapis.com/css2?family=Lato:wght@400;700&display=swap" rel="stylesheet">
<style>
  :root{
    --orange:#f7941d;
    --orange-light:#f9ad52;
    --navy:#323e50;
    --navy-light:#4a5a74;
    --ink:#333a44;
    --muted:#8a8f96;
    --row-a:#e9e9e9;
    --row-b:#f6f6f6;
    --page:#f1f1f1;
    --line:#f28f1e;
    --teal:#2bb8a2;
    --blue:#1f6fb8;
    --sky:#2aa3df;
  }
  *{box-sizing:border-box;margin:0;padding:0}
  html,body{width:1091px;height:1200px;overflow:hidden}
  body{font-family:'Lato',sans-serif;color:var(--ink);background:var(--page);position:relative}
  .topbar{position:absolute;left:0;top:0;width:1091px;height:70px;background:#fff;box-shadow:0 1px 3px rgba(0,0,0,.08)}
  .brand{position:absolute;left:48px;top:14px}
  .brand-name{font-size:27px;font-weight:700;color:var(--navy);line-height:1}
  .brand-tag{font-size:11px;color:var(--muted);margin-top:6px;white-space:nowrap}
  .nav{position:absolute;left:497px;top:30px;display:flex}
  .nav a{font-size:13px;font-weight:700;color:#3a3f47;text-decoration:none;margin-right:25px}
  .logout{position:absolute;left:946px;top:24px;width:98px;height:29px;background:var(--orange);color:#fff;font-weight:700;font-size:14px;display:flex;align-items:center;justify-content:center;gap:7px}
  .panel{position:absolute;background:#fff}
  .panel-head{height:39px;background:var(--orange);color:#fff;display:flex;align-items:center;justify-content:space-between;padding:0 14px}
  .panel-title{font-size:16px;font-weight:700}
  .panel-title.light{font-weight:400}
  .select{border:1px solid #fff;height:25px;display:flex;align-items:center;font-size:12px}
  .select span{padding:0 5px}
  .select i{width:23px;height:100%;border-left:1px solid #fff;display:flex;align-items:center;justify-content:center}
  .accuracy{left:48px;top:91px;width:673px;height:362px;border:1px solid #ddd;border-top:0}
  .impact{left:48px;top:475px;width:673px;height:430px;background:transparent}
  .tabs{height:30px;background:#222;display:flex}
  .tabs div{color:#fff;font-size:13px;padding:0 15px;display:flex;align-items:center;border-right:1px solid #555}
  .tabs div.active{background:#3a3a3a}
  .kpi{left:745px;top:91px;width:299px;height:554px;background:transparent}
  .kpi-summary{background:#fff;height:72px;text-align:center;padding-top:16px}
  .kpi-summary .label{font-size:14px;color:#4a5a74}
  .kpi-summary .value{font-size:13px;font-weight:700;color:#4a5a74;margin-top:1px}
  .kpi-row{height:34px;display:flex;align-items:center;padding:0 9px 0 12px;font-size:11.5px;color:#333}
  .kpi-row:nth-child(odd){background:var(--row-a)}
  .kpi-row:nth-child(even){background:var(--row-b)}
  .kpi-row svg{margin-right:6px;flex:none}
  .kpi-row .v{margin-left:auto}
  .pie-panel{left:745px;width:299px;height:223px;background:#e8e8e8;border:1px solid #d8d8d8;border-top:0}
  .pie-panel .panel-head{position:relative}
  .pie-panel .panel-head::after{content:"";position:absolute;left:141px;bottom:-7px;border:7px solid transparent;border-bottom:0;border-top-color:var(--orange)}
  .footer{position:absolute;left:0;top:1157px;width:1091px;height:43px;background:#2f3b4c;color:#fff;font-size:13px;display:flex;align-items:center;justify-content:center}
  svg text{font-family:'Lato',sans-serif}
</style>
</head>
<body>
<header class="topbar">
  <div class="brand">
    <div class="brand-name">Auditwell</div>
    <div class="brand-tag">Performance Insight</div>
  </div>
  <nav class="nav">
    <a>Accuracy Results</a><a>Processor Accuracy</a><a>Manage Users</a><a>Settings</a>
  </nav>
  <div class="logout">
    <svg width="18" height="15" viewBox="0 0 18 15"><rect x="1" y="1" width="9" height="13" fill="none" stroke="#fff" stroke-width="2"/><path d="M8 7.5h8M13 4l3.5 3.5L13 11" fill="none" stroke="#fff" stroke-width="2"/></svg>
    Logout
  </div>
</header>

<section class="panel accuracy">
  <div class="panel-head"><div class="panel-title">Accuracy Results</div><div class="select"><span>End to End</span><i><svg width="10" height="6"><path d="M1 1l4 4 4-4" fill="none" stroke="#fff" stroke-width="1.6"/></svg></i></div></div>
  <svg width="671" height="323" viewBox="0 0 788 379">
    <text x="395" y="35" text-anchor="middle" font-size="16" fill="#4a5a74">YTD Overall Accuracy</text>
    <text x="395" y="64" text-anchor="middle" font-size="14" fill="#444">Click the bars to view YTD details for the specific region</text>
    <g stroke="#4a5a74" stroke-width="2"><path d="M703 27h16M703 32h16M703 37h16"/></g>
    <g stroke="#e3e3e3"><path d="M74 110H740M74 151H740M74 191H740M74 232H740M74 272H740M74 313H740"/></g>
    <g font-size="11" fill="#555" text-anchor="end"><text x="67" y="114">100</text><text x="67" y="155">97.5</text><text x="67" y="195">95</text><text x="67" y="236">92.5</text><text x="67" y="276">90</text><text x="67" y="317">87.5</text></g>
    <text transform="translate(20 215) rotate(-90)" text-anchor="middle" font-size="14" font-weight="700" fill="#222">Overall Accuracy</text>
    <polyline points="74,313 127,148 194,313 250,134 317,313 374,170 440,313 495,145 561,313 619,199 683,313 728,295 740,313" fill="none" stroke="var(--line)" stroke-width="2"/>
    <g fill="#fff" stroke="var(--line)" stroke-width="2"><circle cx="127" cy="148" r="4"/><circle cx="250" cy="134" r="4"/><circle cx="374" cy="170" r="4"/><circle cx="495" cy="145" r="4"/><circle cx="619" cy="199" r="4"/></g>
    <g font-size="12" fill="#333" text-anchor="middle"><text x="127" y="140">97.7%</text><text x="252" y="126">98.5%</text><text x="375" y="161">96.8%</text><text x="496" y="139">97.7%</text><text x="620" y="191">94.9%</text></g>
    <g font-size="14" fill="#444" text-anchor="middle"><text x="130" y="342">Colorado</text><text x="255" y="342">Georgia</text><text x="381" y="342">Hawaii</text><text x="502" y="342">MidAtlantic</text><text x="628" y="342">NorthWest</text></g>
  </svg>
</section>

<section class="panel impact">
  <div class="panel-head"><div class="panel-title">Error Impact for June 2016</div><div class="select"><span>All Regions</span><i><svg width="10" height="6"><path d="M1 1l4 4 4-4" fill="none" stroke="#fff" stroke-width="1.6"/></svg></i></div></div>
  <div class="tabs"><div class="active">All Errors</div><div>Providers</div><div>Employers</div><div>Line of Business</div></div>
  <svg width="673" height="361" viewBox="0 0 790 424">
    <text x="156" y="32" text-anchor="middle" font-size="19" fill="#444">Top 10 Error Reasons</text>
    <text x="156" y="64" text-anchor="middle" font-size="15" fill="#999">All Regions</text>
    <g stroke="#444" stroke-width="2"><path d="M349 26h17M349 31h17M349 36h17M765 26h17M765 31h17M765 36h17"/></g>
    <text x="574" y="33" text-anchor="middle" font-size="19" fill="#444">Top 10 Error Reasons - Financial Impact</text>
    <text x="574" y="64" text-anchor="middle" font-size="15" fill="#999">All Regions</text>

    <g stroke="#e5e5e5"><path d="M156 89V357M211 89V357M266 89V357M321 89V357M376 89V357"/></g>
    <path d="M156 357H392" stroke="#ccc"/>
    <text transform="translate(10 222) rotate(-90)" text-anchor="middle" font-size="14" font-weight="700" fill="#222">All Errors</text>
    <g font-size="11" fill="#222" text-anchor="end">
      <text x="148" y="108">Incorrect Contract..</text><text x="148" y="134">Claim Paid Incorrectly</text><text x="148" y="160">Not A Halvorn Benefit Bill</text><text x="148" y="187">Incorrect Co-Pay</text><text x="148" y="213">Copay Amount Not Correct</text><text x="148" y="240">Did Not Follow Desk</text><text x="148" y="266">Did Not Follow Pnp</text><text x="148" y="292">Claim Denied in Error</text><text x="148" y="319">Unknown</text><text x="148" y="345">Denied Incorrectly</text>
    </g>
    <polyline points="156,357 222,341 233,315 233,288 260,262 266,236 266,209 282,183 288,156 299,130 348,104" fill="none" stroke="var(--teal)" stroke-width="1.3"/>
    <g fill="#fff" stroke="var(--teal)" stroke-width="1.2"><circle cx="222" cy="341" r="2.8"/><circle cx="233" cy="315" r="2.8"/><circle cx="233" cy="288" r="2.8"/><circle cx="260" cy="262" r="2.8"/><circle cx="266" cy="236" r="2.8"/><circle cx="266" cy="209" r="2.8"/><circle cx="282" cy="183" r="2.8"/><circle cx="288" cy="156" r="2.8"/><circle cx="299" cy="130" r="2.8"/><circle cx="348" cy="104" r="2.8"/></g>
    <g font-size="13" fill="#333"><text x="227" y="347">12</text><text x="238" y="320">14</text><text x="241" y="294">14</text><text x="265" y="267">19</text><text x="270" y="241">20</text><text x="271" y="214">20</text><text x="289" y="187">23</text><text x="295" y="161">24</text><text x="309" y="138">26</text><text x="354" y="109">35</text></g>
    <g font-size="13" fill="#333" text-anchor="middle"><text x="156" y="375">0</text><text x="207" y="377">10</text><text x="263" y="377">20</text><text x="319" y="377">30</text><text x="376" y="377">40</text></g>
    <text x="272" y="414" text-anchor="middle" font-size="14" font-weight="700" fill="#222">Count</text>

    <g stroke="#e5e5e5"><path d="M533 94V362M583 94V362M633 94V362M683 94V362M733 94V362M783 94V362"/></g>
    <path d="M541 94V362" stroke="#ccc"/>
    <g font-size="11" fill="#222" text-anchor="end">
      <text x="531" y="113">Incorrect Contract..</text><text x="531" y="139">Claim Paid Incorrectly</text><text x="531" y="165">Not A Halvorn Benefit Bill</text><text x="531" y="192">Incorrect Co-Pay</text><text x="531" y="218">Copay Amount Not Correct</text><text x="531" y="245">Did Not Follow Desk</text><text x="531" y="271">Did Not Follow Pnp</text><text x="531" y="297">Claim Denied in Error</text><text x="531" y="324">Unknown</text><text x="531" y="350">Denied Incorrectly</text>
    </g>
    <g fill="var(--orange-light)">
      <rect x="568" y="101" width="97" height="17"/><rect x="664" y="127" width="44" height="17"/><rect x="662" y="259" width="52" height="17"/>
      <rect x="733" y="153" width="3" height="17"/><rect x="708" y="180" width="22" height="17"/><rect x="733" y="206" width="3" height="17"/><rect x="733" y="233" width="2" height="17"/><rect x="733" y="285" width="2" height="17"/><rect x="733" y="338" width="3" height="17"/>
    </g>
    <g fill="var(--orange)">
      <rect x="665" y="101" width="98" height="17"/><rect x="708" y="127" width="44" height="17"/><rect x="714" y="259" width="49" height="17"/><rect x="730" y="180" width="10" height="17"/><rect x="734" y="312" width="14" height="17"/>
    </g>
    <g font-size="12" fill="#fff"><text x="580" y="114">$-65155.67</text><text x="673" y="114">$12510.63</text><text x="698" y="140">$2919.39</text><text x="691" y="272">$10390.26</text></g>
    <g font-size="12" fill="#222" text-anchor="end"><text x="660" y="140">$-26915.92</text><text x="725" y="166">$-245</text><text x="704" y="193">$-3898.21</text><text x="725" y="219">$-295</text><text x="730" y="246">$0</text><text x="657" y="272">$-29341.33</text><text x="730" y="298">$0</text><text x="730" y="325">$0</text><text x="730" y="351">$-1.81</text></g>
    <g font-size="12" fill="#222"><text x="744" y="166">$0</text><text x="744" y="219">$10</text><text x="751" y="325">$331.1</text></g>
    <g font-size="13" fill="#333" text-anchor="middle"><text x="537" y="380">-80k</text><text x="583" y="378">-60k</text><text x="633" y="380">-40k</text><text x="683" y="380">-20k</text><text x="733" y="380">0</text><text x="778" y="380">20k</text></g>
    <text x="663" y="416" text-anchor="middle" font-size="14" font-weight="700" fill="#222">$ Amount</text>
  </svg>
</section>

<section class="panel kpi">
  <div class="panel-head"><div class="panel-title">KPI's</div><div class="select"><span>All Regions</span><i><svg width="10" height="6"><path d="M1 1l4 4 4-4" fill="none" stroke="#fff" stroke-width="1.6"/></svg></i></div></div>
  <div class="kpi-summary"><div class="label">Overall YTD Accuracy</div><div class="value">97.41%</div></div>
  <div class="kpi-rows">
    <div class="kpi-row"><svg width="11" height="10"><path d="M5.5 0L11 10H0Z" fill="#333"/><path d="M5.5 3.5v3.2M5.5 7.6v1" stroke="#fff" stroke-width="1.2"/></svg>Claims Audited:<span class="v">4859</span></div>
    <div class="kpi-row"><svg width="11" height="10"><path d="M5.5 0L11 10H0Z" fill="#333"/><path d="M5.5 3.5v3.2M5.5 7.6v1" stroke="#fff" stroke-width="1.2"/></svg>Avg. Claims Audited per day:<span class="v">6.7</span></div>
    <div class="kpi-row"><svg width="11" height="10"><path d="M5.5 0L11 10H0Z" fill="#333"/><path d="M5.5 3.5v3.2M5.5 7.6v1" stroke="#fff" stroke-width="1.2"/></svg>Errors Found:<span class="v">2147</span></div>
    <div class="kpi-row"><svg width="11" height="10"><path d="M5.5 0L11 10H0Z" fill="#333"/><path d="M5.5 3.5v3.2M5.5 7.6v1" stroke="#fff" stroke-width="1.2"/></svg>Financial Impact:<span class="v">$1,462,139</span></div>
    <div class="kpi-row"><svg width="11" height="10"><path d="M5.5 0L11 10H0Z" fill="#333"/><path d="M5.5 3.5v3.2M5.5 7.6v1" stroke="#fff" stroke-width="1.2"/></svg>Total Claims Posted:<span class="v">17,773,591</span></div>
    <div class="kpi-row"><svg width="11" height="10"><path d="M5.5 0L11 10H0Z" fill="#333"/><path d="M5.5 3.5v3.2M5.5 7.6v1" stroke="#fff" stroke-width="1.2"/></svg>Total Encounter Claims:<span class="v">93,984,586</span></div>
    <div class="kpi-row"><svg width="11" height="10"><path d="M5.5 0L11 10H0Z" fill="#333"/><path d="M5.5 3.5v3.2M5.5 7.6v1" stroke="#fff" stroke-width="1.2"/></svg>Total Auto Adjudication Claim Count:<span class="v">920,918</span></div>
    <div class="kpi-row"><svg width="11" height="10"><path d="M5.5 0L11 10H0Z" fill="#333"/><path d="M5.5 3.5v3.2M5.5 7.6v1" stroke="#fff" stroke-width="1.2"/></svg>Total Adjustment Claim Count:<span class="v">920,918</span></div>
    <div class="kpi-row"><svg width="11" height="10"><path d="M5.5 0L11 10H0Z" fill="#333"/><path d="M5.5 3.5v3.2M5.5 7.6v1" stroke="#fff" stroke-width="1.2"/></svg>Total Denied Claim Count:<span class="v">133,523</span></div>
    <div class="kpi-row"><svg width="11" height="10"><path d="M5.5 0L11 10H0Z" fill="#333"/><path d="M5.5 3.5v3.2M5.5 7.6v1" stroke="#fff" stroke-width="1.2"/></svg>Total Dollars Paid:<span class="v">$5,669,835,04</span></div>
    <div class="kpi-row"><svg width="11" height="10"><path d="M5.5 0L11 10H0Z" fill="#333"/><path d="M5.5 3.5v3.2M5.5 7.6v1" stroke="#fff" stroke-width="1.2"/></svg>Auto Adjudication Rate:<span class="v">$0.052</span></div>
    <div class="kpi-row"><svg width="11" height="10"><path d="M5.5 0L11 10H0Z" fill="#333"/><path d="M5.5 3.5v3.2M5.5 7.6v1" stroke="#fff" stroke-width="1.2"/></svg>Adjustment Rate:<span class="v">1.345%</span></div>
    <div class="kpi-row"><svg width="11" height="10"><path d="M5.5 0L11 10H0Z" fill="#333"/><path d="M5.5 3.5v3.2M5.5 7.6v1" stroke="#fff" stroke-width="1.2"/></svg>Denial Rate:<span class="v">0.751%</span></div>
  </div>
</section>

<section class="panel pie-panel" style="top:667px">
  <div class="panel-head"><div class="panel-title light">Paid vs Denied</div><svg width="15" height="12"><path d="M0 1.5h15M0 6h15M0 10.5h15" stroke="#fff" stroke-width="2"/></svg></div>
  <svg width="297" height="183" viewBox="0 0 349 216">
    <circle cx="167" cy="109" r="70" fill="var(--navy)"/>
    <path d="M167 109L167 39A70 70 0 0 0 137 46Z" fill="var(--navy-light)"/>
    <text transform="translate(157 60) rotate(72)" text-anchor="middle" font-size="12" fill="#fff">0.7%</text>
    <text x="167" y="135" text-anchor="middle" font-size="14" font-weight="700" fill="#fff">99.3%</text>
    <rect x="12" y="190" width="13" height="13" fill="var(--blue)"/><text x="33" y="201" font-size="13" font-weight="700" fill="var(--blue)">Denied  : 0.7%</text>
    <rect x="210" y="190" width="13" height="13" fill="var(--sky)"/><text x="232" y="201" font-size="13" font-weight="700" fill="var(--sky)">Paid  : 99.3%</text>
  </svg>
</section>

<section class="panel pie-panel" style="top:912px">
  <div class="panel-head"><div class="panel-title light">Paid vs Encounter</div><svg width="15" height="12"><path d="M0 1.5h15M0 6h15M0 10.5h15" stroke="#fff" stroke-width="2"/></svg></div>
  <svg width="297" height="183" viewBox="0 0 349 216">
    <circle cx="167" cy="109" r="70" fill="var(--navy)"/>
    <path d="M167 109L167 39A70 70 0 0 0 115 62Z" fill="var(--navy-light)"/>
    <text transform="translate(148 60) rotate(60)" text-anchor="middle" font-size="12" fill="#fff">15.9%</text>
    <text x="169" y="134" text-anchor="middle" font-size="13" font-weight="700" fill="#fff">84.1%</text>
    <rect x="12" y="190" width="13" height="13" fill="var(--blue)"/><text x="33" y="201" font-size="13" font-weight="700" fill="var(--blue)">Paid  : 15.9%</text>
    <rect x="193" y="190" width="13" height="13" fill="var(--sky)"/><text x="215" y="201" font-size="13" font-weight="700" fill="var(--sky)">Encounter  : 84.1%</text>
  </svg>
</section>

<footer class="footer">Copyright © 2016 Auditwell.&nbsp;&nbsp; | &nbsp;&nbsp;All rights reserved.</footer>
</body>
</html>
```